Business Card for bespoke luxury cupcakes and cakes
childrens parties, baby showers, seasonal designs, christenings, 3D and 2D designs
Bright & Fun-filled
Tumble Bakes Ltd
London
morvenaltoski@mailnest.co.uk
www.pagelink.co.uk/TumbleBakesLtd

```html
<!DOCTYPE html>
<html lang="en">
<head>
<meta charset="utf-8">
<title>Tumble Bakes Ltd – Business Card</title>
<link href="https://fonts.googleapis.com/css2?family=Questrial&display=swap" rel="stylesheet">
<style>
  :root {
    --backdrop: #e6e6e6;
    --card: #3b332b;
    --card-edge: #2c2620;
    --text-light: #ece8e2;
    --text-soft: #cfc8bd;
    --brand-pink: #e8589a;
    --ribbon: #d8d1b6;
    --ribbon-dark: #a59d82;
    --ribbon-text: #4a4236;
    --band-top: #ffffff;
    --band-bottom: #bdbdbd;
    --band-text: #2f2a24;
  }
  * { margin: 0; padding: 0; box-sizing: border-box; }
  html, body { width: 1200px; height: 898px; overflow: hidden; }
  body {
    background: var(--backdrop);
    font-family: "Questrial", sans-serif;
    position: relative;
  }
  .card {
    position: absolute;
    left: 190px;
    width: 820px;
    height: 390px;
    background: var(--card);
    border-radius: 22px;
    box-shadow: 0 6px 18px rgba(0,0,0,0.25);
    overflow: hidden;
  }
  .card--front { top: 45px; }
  .card--back { top: 463px; }

  /* Front */
  .front-brand {
    position: absolute;
    top: 78px; left: 0; right: 0;
    display: flex; align-items: center; justify-content: center; gap: 18px;
  }
  .brand-dot {
    width: 34px; height: 34px; border-radius: 50%;
    background: var(--brand-pink);
  }
  .brand-name {
    color: var(--brand-pink);
    font-size: 64px;
    line-height: 1;
    letter-spacing: 1px;
  }
  .ribbon {
    position: absolute;
    top: 190px; left: 50%;
    transform: translateX(-50%);
    width: 470px; height: 58px;
  }
  .ribbon-label {
    position: absolute; inset: 0;
    display: flex; align-items: center; justify-content: center;
    color: var(--ribbon-text);
    font-size: 26px;
    letter-spacing: 0.5px;
  }
  .front-url {
    position: absolute;
    right: 44px; bottom: 34px;
    color: var(--text-light);
    font-size: 21px;
    letter-spacing: 0.5px;
  }

  /* Back */
  .back-brand {
    position: absolute;
    top: 38px; left: 170px;
    display: flex; flex-direction: column; align-items: flex-start;
  }
  .back-brand .brand-row { display: flex; align-items: center; gap: 10px; }
  .back-brand .brand-dot { width: 20px; height: 20px; }
  .back-brand .brand-name { font-size: 38px; }
  .back-brand .brand-sub {
    margin-top: 4px; margin-left: 30px;
    color: var(--brand-pink);
    font-size: 17px;
  }
  .tagline {
    position: absolute;
    top: 132px; left: 150px; right: 40px;
    color: var(--text-light);
    font-size: 31px;
    line-height: 1.12;
    text-align: center;
  }
  .contact-band {
    position: absolute;
    left: 0; right: 0; top: 222px; height: 100px;
    background: linear-gradient(180deg, var(--band-top) 0%, #e4e4e4 55%, var(--band-bottom) 100%);
  }
  .contact-list {
    position: absolute;
    top: 236px; left: 0; right: 0;
    text-align: center;
    color: var(--band-text);
    font-size: 22px;
    line-height: 1.35;
    list-style: none;
  }
  .contact-list span { margin-right: 14px; }
  .back-url {
    position: absolute;
    left: 44px; bottom: 26px;
    color: var(--text-soft);
    font-size: 20px;
    letter-spacing: 0.5px;
  }
</style>
</head>
<body>

  <section class="card card--front" aria-label="Business card front">
    <div class="front-brand">
      <span class="brand-dot"></span>
      <span class="brand-name">Tumble Bakes</span>
    </div>
    <div class="ribbon">
      <svg width="470" height="58" viewBox="0 0 470 58" aria-hidden="true">
        <polygon points="0,14 40,14 40,58 0,58 14,36" fill="var(--ribbon-dark)"/>
        <polygon points="470,14 430,14 430,58 470,58 456,36" fill="var(--ribbon-dark)"/>
        <rect x="24" y="4" width="422" height="46" fill="var(--ribbon)"/>
      </svg>
      <div class="ribbon-label">Tumble Bakes Ltd</div>
    </div>
    <p class="front-url">www.pagelink.co.uk/TumbleBakesLtd</p>
  </section>

  <section class="card card--back" aria-label="Business card back">
    <div class="back-brand">
      <div class="brand-row">
        <span class="brand-dot"></span>
        <span class="brand-name">Tumble Bakes</span>
      </div>
      <span class="brand-sub">Tumble Bakes Ltd</span>
    </div>
    <p class="tagline">Bespoke cupcakes and cake designs<br>for any occasion</p>
    <div class="contact-band"></div>
    <ul class="contact-list">
      <li><span>Phone</span>+44 7700 900 417</li>
      <li>Email morvenaltoski@mailnest.co.uk</li>
    </ul>
    <p class="back-url">www.pagelink.co.uk/TumbleBakesLtd</p>
  </section>

</body>
</html>
```